Tolvene Hub Redesign

tolvenehub.com is one of our old, high-traffic multilingual site.

its interface is very old, so we want to redesign it to give a modern, attractive design, with comfortable colors and layout.

beside the current content of the main page we want to add two places for dynamic banners.

The site has an App in Phone App and Tablet App, we want an ad in a noticeable place for it.

this ad will be permanent.

the site now has 12 languages, but we may add new languages soon, so design must consider this.

redesign of two internal pages also required:
- the main listing page, example: http://www.tolvenehub.example/en/cat/252
- the article view page: http://www.tolvenehub.example/en/10323

Reason: want to receive more designs ...

```html
<!DOCTYPE html>
<html lang="en">
<head>
<meta charset="utf-8">
<title>Tolvene Hub — Questions &amp; Answer</title>
<link href="https://fonts.googleapis.com/css2?family=Arimo:wght@400;700&family=Roboto+Condensed:wght@400;700&display=swap" rel="stylesheet">
<style>
:root{
  --green:#2f8f36;
  --green-dark:#23772a;
  --ink:#222;
  --text:#333;
  --muted:#777;
  --line:#d9d9d9;
  --dark:#3a3a3a;
  --footer:#4a4a4a;
  --footer-bottom:#333;
  --paper:#fff;
}
*{box-sizing:border-box;margin:0;padding:0}
html,body{width:1002px;height:1200px;overflow:hidden;background:var(--paper)}
body{position:relative;font-family:"Arimo",Arial,sans-serif;color:var(--text);font-size:10px}
.abs{position:absolute}
ul{list-style:none}

/* header */
.brand{left:134px;top:18px;display:flex;align-items:center;gap:8px}
.brand-dot{width:26px;height:26px;border-radius:50%;background:var(--green)}
.brand-name{font-family:"Roboto Condensed",sans-serif;font-weight:700;font-size:36px;color:var(--ink);line-height:1}
.brand-tag{left:207px;top:75px;font-size:13px;color:var(--text)}
.book{left:404px;top:20px;width:92px;height:74px;border-radius:6px;background:linear-gradient(135deg,#c9b25a,#6b4b2a)}
.scholar{left:508px;top:39px;font-size:12.5px;color:var(--text);line-height:16px}
.scholar strong{display:block;color:var(--green);font-size:13px;letter-spacing:.5px}
.apps{left:702px;top:4px;width:165px;height:56px;background:#efefef;display:flex;align-items:center;justify-content:space-around;padding:0 10px}
.app{display:flex;align-items:center;gap:5px;font-size:11px;font-weight:700;color:#555}
.app i{width:14px;height:14px;background:var(--green);display:block}
.app:first-child i{background:#777}
.date{right:135px;top:79px;font-size:10px;color:var(--green)}

/* nav */
.nav{left:134px;top:113px;width:733px;height:29px;display:flex;background:var(--green)}
.nav a{color:#fff;text-decoration:none;font-size:9.5px;display:flex;align-items:center;justify-content:center;border-left:1px solid #4aa851}
.nav a.active{background:var(--dark);border-left:none}

/* toolbar */
.lang-label{left:134px;top:156px;font-size:11px;color:var(--ink)}
.select{left:186px;top:153px;width:142px;height:19px;border:1px solid #ccc;font-size:10px;color:#555;padding:3px 5px}
.select b{position:absolute;right:3px;top:3px;width:11px;height:11px;border:1px solid #aaa;background:#f2f2f2}
.search{left:346px;top:153px;width:348px;height:20px;border:1px solid #ccc;font-size:9.5px;color:#666;padding:4px 7px}
.search-btn{right:0;top:-1px;width:50px;height:20px;background:var(--dark);color:#fff;font-size:10px;display:flex;align-items:center;justify-content:center}
.adv{left:701px;top:156px;font-size:10px;color:var(--muted);text-decoration:underline}
.social{display:flex;gap:8px}
.social i{width:18px;height:18px;border-radius:3px;display:block}
.s1{background:#3b5a99}.s2{background:#2aa5dd}.s3{background:#f39a1e}
.top-social{left:797px;top:154px}
.rule{left:134px;top:186px;width:733px;height:1px;background:#e6e6e6}

/* banners */
.banner{top:202px;width:359px;height:246px;overflow:hidden}
.banner-img{height:212px;width:100%}
.banner-bar{height:34px;background:var(--green);color:#fff;font-family:"Roboto Condensed",sans-serif;font-size:21px;display:flex;justify-content:space-between;align-items:center;padding:0 10px}
.banner-bar span:last-child{font-size:20px}

/* tabs & lists */
.tab{top:472px;height:28px;font-size:12.5px;display:flex;align-items:center;justify-content:center;border:1px solid var(--line);border-bottom:none;color:var(--text);background:#fff}
.tab.on{background:var(--dark);color:#fff;border-color:var(--dark)}
.cat-box{left:134px;top:499px;width:258px;height:331px;border:1px solid var(--line);border-radius:2px;box-shadow:0 1px 2px rgba(0,0,0,.08)}
.tick-list li{position:relative;padding-left:18px;font-size:10px;line-height:12px;color:var(--ink)}
.tick-list li::before{content:"";position:absolute;left:2px;top:1px;width:4px;height:7px;border:solid #999;border-width:0 2px 2px 0;transform:rotate(40deg)}
.cat-list{left:148px;top:518px}
.cat-list li{margin-bottom:14.4px}
.btn{height:25px;background:var(--green);color:#fff;font-weight:700;font-size:10px;display:flex;align-items:center;justify-content:center;gap:8px;border-radius:2px}
.btn::after{content:"";width:5px;height:5px;border:solid #fff;border-width:2px 2px 0 0;transform:rotate(45deg)}

.section-title{left:434px;top:470px;font-family:"Roboto Condensed",sans-serif;font-size:21px;color:var(--ink)}
.arrows{left:826px;top:476px;display:flex;gap:4px}
.arrows i{width:18px;height:18px;border-radius:50%;display:flex;align-items:center;justify-content:center}
.arrows i::after{content:"";width:4px;height:4px;border:solid #fff;border-width:2px 2px 0 0}
.arrows .prev{background:var(--dark)}.arrows .prev::after{transform:rotate(-135deg);margin-left:2px}
.arrows .next{background:var(--green)}.arrows .next::after{transform:rotate(45deg);margin-right:2px}
.title-rule{left:434px;top:499px;width:433px;height:1px;background:#cfcfcf}
.fatwas{left:434px;top:515px;width:433px}
.fatwas li{position:relative;padding-left:11px;font-size:9.6px;line-height:12px;color:var(--ink);margin-bottom:13.6px}
.fatwas li::before{content:"»";position:absolute;left:0;top:0}

/* lower panel */
.panel{left:134px;top:847px;width:733px;height:199px;border:1px solid var(--line);border-radius:2px}
.ptabs{display:flex;height:36px;border-bottom:1px solid var(--line)}
.ptabs div{display:flex;align-items:center;justify-content:center;text-align:center;font-size:10.5px;line-height:12px;color:var(--green-dark);border-left:1px solid var(--line)}
.ptabs div.on{background:var(--dark);color:#fff;border-left:none}
.counsel{left:148px;top:904px;width:680px}
.counsel li{margin-bottom:10.6px}

/* footer */
.footer{left:0;top:1062px;width:1002px;height:113px;background:var(--footer);color:#fff}
.footer-bottom{left:0;top:1175px;width:1002px;height:25px;background:var(--footer-bottom);color:#ccc;font-size:10px;display:flex;align-items:center;justify-content:center;gap:4px}
.footer-bottom b{color:var(--green);font-weight:400}
.fcol h4{font-size:10px;font-weight:700;margin-bottom:15px}
.fcol li{font-size:9.5px;line-height:13.2px}
.fhead{font-size:13px;font-weight:700}
.vline{width:1px;height:82px;background:#666;top:14px}
.email{left:707px;top:41px;width:160px;height:22px;background:#fff;border:1px solid #ccc;color:#999;font-size:9px;padding:5px 7px}
.signup{left:708px;top:69px;width:54px;height:21px;background:var(--green);font-weight:700;font-size:10.5px;display:flex;align-items:center;justify-content:center;border-radius:2px}
</style>
</head>
<body>

<header>
  <div class="abs brand"><span class="brand-dot"></span><span class="brand-name">Tolvene Hub</span></div>
  <div class="abs brand-tag">Questions &amp; Answer</div>
  <div class="abs book" role="img" aria-label="Ornate holy book resting on a wooden stand"></div>
  <div class="abs scholar">SHAYKH HARUN`S<strong>AL - MEDAVI</strong></div>
  <div class="abs apps"><span class="app"><i></i>Phone App</span><span class="app"><i></i>Tablet App</span></div>
  <div class="abs date">Fri 11 Muh 1435 - 15 November 2013</div>
</header>

<nav class="abs nav">
  <a class="active" style="width:68px">HOME</a>
  <a style="width:94px">CATAGORIES</a>
  <a style="width:96px">NEW FATWAS</a>
  <a style="width:85px">ABOUT US</a>
  <a style="width:118px">ARTICLE &amp; BOOKS</a>
  <a style="width:126px">SEND A QUESTIONS</a>
  <a style="width:146px">INTRODUCTION OF ISLAM</a>
</nav>

<div class="abs lang-label">Language</div>
<div class="abs select">English<b></b></div>
<div class="abs search">Search key word ...<span class="abs search-btn">Search</span></div>
<div class="abs adv">Advance Search</div>
<div class="abs social top-social"><i class="s1"></i><i class="s2"></i><i class="s3"></i></div>
<div class="abs rule"></div>

<section class="abs banner" style="left:134px">
  <div class="banner-img" role="img" aria-label="Crowd of pilgrims around the Kaaba under a blue sky" style="background:linear-gradient(180deg,#aac6e0 0%,#d6dde3 45%,#b8ab93 70%,#8f887c 100%)"></div>
  <div class="banner-bar"><span>Memorization of Quran</span><span>»</span></div>
</section>
<section class="abs banner" style="left:509px">
  <div class="banner-img" role="img" aria-label="Black and white photo of a woman praying in a quiet room" style="background:linear-gradient(120deg,#2a2a2a 0%,#6d6d6d 45%,#bdbdbd 75%,#5a5a5a 100%)"></div>
  <div class="banner-bar"><span>Secrets of Islum</span><span>»</span></div>
</section>

<div class="abs tab on" style="left:181px;width:78px">Catagories</div>
<div class="abs tab" style="left:266px;width:78px">Files</div>
<div class="abs cat-box"></div>
<ul class="abs tick-list cat-list">
  <li>Basic Tenets of Faith.</li>
  <li>The Quraan and its Sciences.</li>
  <li>Hadeeth &amp; its Sciences.</li>
  <li>Rulings on Jihaad.</li>
  <li>Fiqh of the family.</li>
  <li>Islamic history and biography.</li>
  <li>Enjoining what is good and forbidding what is evil.</li>
  <li>Pedagogy education and upbringing.</li>
  <li>Psychological and Social Problems.</li>
  <li>Islamic politics.</li>
</ul>
<div class="abs btn" style="left:148px;top:793px;width:83px">Read More</div>

<h2 class="abs section-title">New Fatwas</h2>
<div class="abs arrows"><i class="prev"></i><i class="next"></i></div>
<div class="abs title-rule"></div>
<ul class="abs fatwas">
  <li>Ruling on working with companies that do surveys on the Internet.</li>
  <li>Ruling on singling out ‘Ashoora for fasting.</li>
  <li>He noticed a smell but did not feel any wind coming out of him.</li>
  <li>Eating food that is made for ‘Ashoora’.</li>
  <li>Hijab in Islam is not due to sexual obsession.</li>
  <li>Will the person who intends to fast ‘Ashoora during the day be rewarded for his fasting?</li>
  <li>Recommendation to fast Taasoo’a’ with ‘Ashoora’.</li>
  <li>‘Aashoora’ in Islam and previous religions, and refutation of the Raafidi claim that it is an innovation introduced by the Umayyads.</li>
  <li>Her husband reviles Islam and does not pray, but if she gets divorced from him, she will be forced to work and take off her hijab.</li>
  <li>The virtue of fasting ‘Ashoora’.</li>
</ul>
<div class="abs btn" style="left:434px;top:792px;width:128px">View All New Fatwas</div>

<section class="abs panel">
  <div class="ptabs">
    <div class="on" style="width:110px">Counselling</div>
    <div style="width:134px">Jurisprudence of<br>Acts of Worship</div>
    <div style="width:142px">Jurisprudence of<br>Muslim Minorities</div>
    <div style="width:126px">Contemporary<br>Transactions</div>
    <div style="width:117px">Basic Tenets<br>of Faith</div>
    <div style="width:104px">The Muslim<br>Woman</div>
  </div>
</section>
<ul class="abs tick-list counsel">
  <li>Her fiancé refuses to let her wear hijab.</li>
  <li>His wife torments his daughter from another wife, and he has a son from her, and he is confused as to how he should deal with her.</li>
  <li>A woman asking for a divorce from her husband who is addicted to drugs.</li>
  <li>He did the marriage contract with her and was intimate with her without intercourse in Ramadaan, and he had intercourse with her before announcing the marriage!</li>
</ul>
<div class="abs btn" style="left:149px;top:1008px;width:83px">Read More</div>

<footer class="abs footer">
  <div class="abs fcol" style="left:135px;top:15px">
    <h4>Information</h4>
    <ul><li>» Home</li><li>» About us</li><li>» Introduction of Islam</li><li>» Contact Us</li></ul>
  </div>
  <div class="abs vline" style="left:277px"></div>
  <div class="abs fcol" style="left:325px;top:15px">
    <h4>Usefull Links</h4>
    <ul><li>» Catagories</li><li>» New Fatwas</li><li>» Article &amp; Books</li><li>» Send a Questions</li></ul>
  </div>
  <div class="abs vline" style="left:462px"></div>
  <div class="abs fhead" style="left:518px;top:14px">Follow us on</div>
  <div class="abs social" style="left:520px;top:43px"><i class="s1"></i><i class="s2"></i><i class="s3"></i></div>
  <div class="abs vline" style="left:658px"></div>
  <div class="abs fhead" style="left:707px;top:14px">Signup News Letter</div>
  <div class="abs email">Enter your Email ...</div>
  <div class="abs signup">Signup</div>
</footer>
<div class="abs footer-bottom">Copyright © <b>Tolvene Hub</b> 2013 44.78. All Right Reserved.</div>

</body>
</html>
```